RT Blacktop Works needs awesome postcard design

Business to business post card design needed. We are an asphalt paving contractor looking to attract commercial and industrial customers who need pavement replacement and repairs. We do: Asphalt paving, milling, crack filling and striping.

Postcard should have the following words:
RT Blacktop Works
www.rtblacktopworks.example
Asphalt Paving
Milling
Hot Rubber Crack Filling
Striping

The Region's Trusted Paving Contractor
(555) 827-1963

Address for return area on card:
RT Blacktop Works
48213 Fenwick
Harlow Springs, MI 00000

Target Market(s)

Building owners and property managers

Industry/Entity Type

Ashpalt Paving

Font styles to use
Sans Serif

Requirements
Must have
• Logo, phone number (555) 827-1963, tagline: "The Region's Trusted Paving Contractor" website address and: Paving, milling, hot rubber crack filling, seal coating
Nice to have
• Picture of a newly paved parking lot with or without stripes
Should not have
• Homeowner driveway - WE DO NOT WANT TO ATTRACT RESIDENTIAL WORK

```html
<!DOCTYPE html>
<html lang="en">
<head>
<meta charset="utf-8">
<title>RT Blacktop Works Postcard</title>
<link href="https://fonts.googleapis.com/css2?family=Roboto+Condensed:wght@300;400;700&display=swap" rel="stylesheet">
<style>
  :root {
    --stage: #7a7a7a;
    --paper: #ffffff;
    --ink: #000000;
    --soft-ink: #e6e6e6;
  }
  * { margin: 0; padding: 0; box-sizing: border-box; }
  html, body {
    width: 1199px; height: 1200px; overflow: hidden;
    background: var(--stage);
    font-family: "Roboto Condensed", Arial, sans-serif;
  }
  .postcard {
    position: absolute;
    width: 648px; height: 431px;
    background: var(--paper);
    transform-origin: 0 0;
    transform: scale(1.2485);
    box-shadow: 0 1px 3px rgba(0,0,0,.35);
    overflow: hidden;
    color: var(--ink);
  }
  .postcard--front { left: 195px; top: 44px; }
  .postcard--back  { left: 195px; top: 617px; }
  .shapes { position: absolute; inset: 0; width: 648px; height: 431px; }
  .brand-lockup {
    position: absolute; left: 30px; top: 48px; width: 192px;
    text-align: center;
  }
  .brand-lockup__name {
    display: flex; align-items: center; justify-content: center; gap: 6px;
    font-weight: 700; font-size: 21px; line-height: 1; letter-spacing: .2px;
  }
  .brand-lockup__mark { width: 12px; height: 12px; background: var(--ink); flex: none; }
  .brand-lockup__line { font-weight: 700; font-size: 9px; line-height: 12px; letter-spacing: .3px; }
  .brand-lockup__line:first-of-type { margin-top: 10px; }
  .company-title {
    position: absolute; left: 32px;
    font-weight: 700; font-size: 27px; line-height: 1; letter-spacing: .3px;
  }
  .company-url { position: absolute; left: 32px; font-size: 15px; line-height: 1; }
  .postcard--front .company-title, .postcard--front .company-url { color: var(--paper); }
  .postcard--front .company-title { top: 171px; }
  .postcard--front .company-url { top: 202px; }
  .postcard--back .company-title { top: 286px; }
  .postcard--back .company-url { top: 319px; }
  .services { position: absolute; left: 32px; top: 266px; list-style: none; }
  .services li { font-size: 16px; line-height: 21.7px; display: flex; align-items: center; }
  .services li::before { content: "✸"; font-size: 14px; width: 25px; }
  .tagline {
    position: absolute; right: 41px; top: 200px; text-align: right;
    color: var(--paper);
  }
  .tagline__text { font-size: 22px; font-weight: 400; line-height: 29px; }
  .tagline__phone { font-size: 17px; line-height: 21px; }
  .return-address {
    position: absolute; right: 41px; top: 310px; text-align: right;
    color: var(--paper); font-style: normal;
  }
  .return-address__label { font-weight: 700; font-size: 16px; line-height: 22px; }
  .return-address__line { font-weight: 300; font-size: 15px; line-height: 22px; color: var(--soft-ink); }
</style>
</head>
<body>

<section class="postcard postcard--front">
  <svg class="shapes" viewBox="0 0 648 431" aria-hidden="true">
    <polygon points="0,162 392,162 324,230 0,230" fill="var(--ink)"/>
    <polygon points="524,40 648,164 648,431 137,431" fill="var(--ink)"/>
  </svg>
  <div class="brand-lockup">
    <div class="brand-lockup__name"><span class="brand-lockup__mark"></span>RT Blacktop Works</div>
    <div class="brand-lockup__line">555.827.1963</div>
    <div class="brand-lockup__line">WWW.RTBLACKTOPWORKS.EXAMPLE</div>
  </div>
  <h1 class="company-title">RT BLACKTOP WORKS</h1>
  <div class="company-url">www.rtblacktopworks.example</div>
  <ul class="services">
    <li>Asphalt Paving</li>
    <li>Milling</li>
    <li>Hot Rubber Crack Filling</li>
    <li>Striping</li>
  </ul>
  <div class="tagline">
    <div class="tagline__text">The Region's Trusted<br>Paving Contractor</div>
    <div class="tagline__phone">(555) 827-1963</div>
  </div>
  <address class="return-address">
    <div class="return-address__label">Address for return area on card:</div>
    <div class="return-address__line">RT Blacktop Works</div>
    <div class="return-address__line">48213 Fenwick</div>
    <div class="return-address__line">Harlow Springs, MI 00000</div>
  </address>
</section>

<section class="postcard postcard--back">
  <svg class="shapes" viewBox="0 0 648 431" aria-hidden="true">
    <polygon points="254,0 324,0 324,321 307,321 281,236 254,252" fill="var(--ink)"/>
    <rect x="517.5" y="31.5" width="89" height="91" fill="none" stroke="var(--ink)" stroke-width="1.5"/>
    <line x1="366" y1="335" x2="606" y2="335" stroke="var(--ink)" stroke-width="1.5"/>
    <line x1="366" y1="372" x2="606" y2="372" stroke="var(--ink)" stroke-width="1.5"/>
  </svg>
  <div class="brand-lockup">
    <div class="brand-lockup__name"><span class="brand-lockup__mark"></span>RT Blacktop Works</div>
    <div class="brand-lockup__line">555.827.1963</div>
    <div class="brand-lockup__line">WWW.RTBLACKTOPWORKS.EXAMPLE</div>
  </div>
  <h2 class="company-title">RT BLACKTOP WORKS</h2>
  <div class="company-url">www.rtblacktopworks.example</div>
</section>

</body>
</html>
```